Need a small Brochure Designing for a High Tech LED Spotlight

This is an expensive product and the best of it's kind in the world, so it needs to be marketed to intelligent, forward thinking people who appreciate and pay for excellent design and innovation. The type of people who buy Quince products i guess. It needs to be clean. The colours do not need to be in keep with our website, but our logo does need to be on the brochure. I have attached a dcoument with all the text, the order the text goes in and an idea of how i want the first page to look. All images and logos have been attached too.

Target Market(s)

This is aimed at people with high disposible incomes who spend money on the best designed products and the latest technology. The type of people who buy Quince products.

Industry/Entity Type

Product

Requirements
Must have
• The work needs to be editable by us using indesign

The pages need to be A5. I'm not sure how many pages the brochure needs to be as it does need to be clean and be spaced out well. On the file that contains the text i've indicated that 8 pages would be good.

The logos i attached - 1) Kelo Product Design Award, 2) Z Technology Award, 3) Blue Fern Design Award and 4) Keen Design Award all need to be at the bottom of the front page, quite small, but still able to see them well.

- Needs to have a QR code so that smart phones can scan the code and be taken to a pol vane clip - QR code is attached.
- Needs to have Plimbo Icon - @KestrowHomeCo
Nice to have
• Nice to remind customers on each page that the product has a 5 year Warranty and we have a 365 day Returns Policy.

```html
<!DOCTYPE html>
<html lang="en">
<head>
<meta charset="utf-8">
<title>K7 LED Spotlight Brochure Spreads</title>
<link rel="stylesheet" href="https://fonts.googleapis.com/css2?family=Lato:ital,wght@0,300;0,400;0,700;1,400&display=swap">
<style>
  :root {
    --backdrop: #c9b7a3;
    --paper: #ffffff;
    --accent-red: #d8262e;
    --ink: #3a3a3a;
    --ink-soft: #555555;
    --fold: #d6d6d6;
    --wood: #c98e58;
    --wood-dark: #8a5a33;
    --wall: #f1ece4;
    --night: #2c3350;
  }
  * { box-sizing: border-box; margin: 0; padding: 0; }
  html, body { width: 1200px; height: 1000px; overflow: hidden; }
  body {
    background: var(--backdrop);
    font-family: "Lato", Arial, sans-serif;
    position: relative;
  }
  .spread {
    position: absolute;
    left: 124px;
    width: 953px;
    height: 336px;
    background: var(--paper);
  }
  .spread--testimonials { top: 143px; }
  .spread--promise { top: 521px; }

  .headline {
    position: absolute;
    color: var(--accent-red);
    font-weight: 300;
    font-size: 18px;
    line-height: 23px;
  }
  .spread--testimonials .headline { left: 29px; top: 26px; width: 140px; }
  .spread--promise .headline { left: 29px; top: 26px; width: 150px; }
  .headline p + p { margin-top: 23px; }

  .quote-col {
    position: absolute;
    top: 27px;
    width: 136px;
    font-size: 7.4px;
    line-height: 10.4px;
    color: var(--ink);
  }
  .quote-col .quote { font-style: italic; }
  .quote-col .quote + .quote,
  .quote-col .author + .quote { margin-top: 10px; }
  .quote-col .author {
    text-align: right;
    font-style: normal;
    margin-top: 2px;
  }
  .col-a { left: 171px; }
  .col-b { left: 314px; }
  .col-c { left: 504px; width: 134px; }

  .page-fold {
    position: absolute;
    left: 476px;
    top: 0;
    width: 1px;
    height: 336px;
    background: var(--fold);
  }

  .photo-kitchen {
    position: absolute;
    left: 648px;
    top: 0;
    width: 305px;
    height: 336px;
    background: linear-gradient(180deg, #f3f0ec 0%, #e9e4dd 48%, #d49a62 62%, var(--wood) 100%);
  }
  .photo-courtyard {
    position: absolute;
    left: 172px;
    top: 0;
    width: 498px;
    height: 336px;
    background: linear-gradient(180deg, #c9d3e4 0%, var(--night) 30%, #e8d3a8 55%, var(--wood) 78%, var(--wood-dark) 100%);
  }

  .partner-list {
    position: absolute;
    left: 670px;
    top: 0;
    width: 283px;
    height: 336px;
    list-style: none;
  }
  .partner {
    position: absolute;
    display: flex;
    align-items: center;
    gap: 6px;
    color: var(--ink);
    font-family: "Lato", Arial, sans-serif;
    font-weight: 400;
    font-size: 16px;
    white-space: nowrap;
  }
  .partner-mark {
    width: 22px; height: 22px;
    border-radius: 50%;
    background: var(--ink-soft);
  }
  .p1 { left: 36px; top: 31px; }
  .p2 { right: 30px; top: 67px; }
  .p3 { left: 36px; top: 178px; }
  .p4 { right: 30px; top: 205px; }
  .p5 { left: 36px; top: 266px; }
</style>
</head>
<body>

<section class="spread spread--testimonials">
  <h2 class="headline">Customers who have bought K7 rate it at 96%</h2>

  <div class="quote-col col-a">
    <p class="quote">"It's an incredibly impressive product. When you see and hold the product it oozes quality.</p>
    <p class="quote">The quality of the light was something else and it really made everything in the flat seem clearer. Our wine glasses looked brand new under these spots. Backed up with a 5 year warranty and a believable 40,000 hour lifespan (about 18 years) then it's certainly the product I would buy in a heart beat if my name began with Sheikh or ended in Vanderholt."</p>
    <p class="author">LED Reviewer &amp; Blogger Jon</p>
    <p class="quote">"The electrician who installed the lights compared them to a regular 50 watt light and we both agreed the light quality and colour was superior on the K7! A more energy efficient light and a better quality light, a win, win situation."</p>
    <p class="author">Adrian</p>
    <p class="quote">"A superb spotlight that does all the seller says it does. An incredible</p>
  </div>

  <div class="quote-col col-b">
    <p class="quote">amount of light for such a low wattage."</p>
    <p class="author">Cris</p>
    <p class="quote">"Once fitted they were more than I expected, brilliantly bright, but not too harsh , as I had ordered the warm white I cannot recommend them enough, they're great.</p>
    <p class="author">Simon</p>
    <p class="quote">When you see the results, the light is incredible. The 135 degree beam angle fills my room much better than the previous 60 degree, there's very few (if any) dark spots now. I plumped for the "daytime" (natural white) colour, it does exactly as described, at midnight with the lights on it could be mistaken for noon – very, very impressed.</p>
    <p class="author">Matt</p>
    <p class="quote">I own a large apartment in Chelsea on the river and was sick and tired of having to replace blown halogens all the time. I believe in investing in the best quality products possible and the K7 7w LED Spot is certainly</p>
  </div>

  <div class="page-fold"></div>

  <div class="quote-col col-c">
    <p class="quote">that. The product is exceptionally well designed, produces a light quality that is a vast improvement on my old halogens and I can control the lighting using the existing Lumora system. &nbsp;The 1 year returns period really hammers home how much the company believes in the product.</p>
    <p class="author">Ryan</p>
    <p class="quote">I would like to compliment you and your team at Kestrow Home. Every question I asked, you responded to in a very professional way. The quality of your product is first class including delivery. All in all I have been extremely impressed and would have no hesitation in using you and your team again.</p>
    <p class="author">Dave at RT Builders</p>
  </div>

  <div class="photo-kitchen" role="img" aria-label="Photo of a bright white kitchen with pendant lights, an island with bar stools and a timber floor"></div>
</section>

<section class="spread spread--promise">
  <div class="headline">
    <p>5 year<br>Warranty.</p>
    <p>365 day<br>Returns Policy.</p>
    <p>Best brands<br>trusts K7.</p>
  </div>

  <div class="photo-courtyard" role="img" aria-label="Photo of a modern home at dusk seen from a timber deck, glass doors open to a lit dining and living room"></div>

  <ul class="partner-list">
    <li class="partner p1"><span class="partner-mark"></span>Verano Motors</li>
    <li class="partner p2">Tashiro</li>
    <li class="partner p3">The Halden House</li>
    <li class="partner p4">Marrow</li>
    <li class="partner p5">Brisk</li>
  </ul>
</section>

</body>
</html>
```